Design for Torvel Ginger Chewy Candy!

Hello! We are Torvel Enterprises Corp, a food manufacturer and distributor based in Los Angeles, CA. We manufacture Chips, Cookies, Juices, Dairy, and last but not least, Candies! We are launching our Ginger Chewy Candy soon and we need a great design for it!

Our Ginger Chewy Candy is a perfect mixture between sweet and spicy from the ginger itself. Torvel Ginger Chewy Candy a good relief for sore throat and nausea.

Now, other than a great design, we also welcome brand suggestions for the candy.
If you can come up with a logo for the Ginger Candy, that would be swell!

We are open to unique and out of the box design. We chose a few color schemes for the design, but feel free to step out of the box if you feel it suits the brand.

We don't have the exact size for the plastic pouch, but it should be a generic small plastic pouch size (approximately 4 oz resealable plastic pouch)

Please have fun designing the project, we can't wait to see all the great designs!

Cheers!

Target Market(s)

USA and Asian market
Age 30-70
Male and Female

Industry/Entity Type

Manufacture

Font styles to use
Serif
Sans Serif
Decorative

Colors
fff3d1
fee18a
fece3e
fbc994
fce8d3

Requirements
Must have
• Torvel Logo
• A picture of ginger (illustrations or photographs are welcome)
Nice to have
• Coating suggestions like Matte surface or SPOT UV
• Give us ideas of what the name of the chewy candy should be. Product name ideas are welcome!

```html
<!DOCTYPE html>
<html lang="en">
<head>
<meta charset="utf-8">
<title>Torvel Ginger Chewy Candy – 4oz Pouch</title>
<link href="https://fonts.googleapis.com/css2?family=Anton&family=Lilita+One&family=PT+Sans:wght@400;700&display=swap" rel="stylesheet">
<style>
  :root {
    --pouch-yellow: #f5d92f;
    --deep-yellow: #fece3e;
    --soft-orange: #fbc994;
    --cream: #fff3d1;
    --navy: #2b2a7c;
    --gold-stroke: #e9a91c;
    --dieline: #9fdcf2;
    --page: #ffffff;
  }
  * { margin: 0; padding: 0; box-sizing: border-box; }
  html, body { width: 920px; height: 1200px; overflow: hidden; background: var(--page); }
  .canvas { position: relative; width: 920px; height: 1200px; }

  .spec-note {
    position: absolute; left: 78px; top: 26px;
    font: 400 18px/1 "PT Sans", sans-serif;
    color: var(--dieline);
  }

  .dieline { position: absolute; left: 0; top: 0; }

  .brand-name {
    position: absolute; left: 0; width: 858px; top: 288px;
    text-align: center;
    font: 700 58px/1 "PT Sans", sans-serif;
    color: var(--navy);
    letter-spacing: -1px;
  }

  .product-title {
    position: absolute; left: 170px; top: 400px;
    font: 400 168px/1 "Lilita One", sans-serif;
    color: #fffdf3;
    -webkit-text-stroke: 14px var(--navy);
    paint-order: stroke fill;
    transform: rotate(-12deg);
    transform-origin: left top;
    letter-spacing: -2px;
  }

  .product-subtitle {
    position: absolute; left: 393px; top: 588px;
    font: 400 52px/1 "Anton", sans-serif;
    color: #fffdf3;
    -webkit-text-stroke: 7px var(--navy);
    paint-order: stroke fill;
    transform: rotate(-12deg);
    transform-origin: left top;
  }

  .candy-photo {
    position: absolute; left: 171px; top: 640px;
    width: 627px; height: 305px;
    border-radius: 46% 52% 40% 44% / 50% 48% 52% 50%;
    background: radial-gradient(ellipse at 45% 55%, #f7b93a 0%, #fbcf5a 55%, #fde6a0 100%);
  }
</style>
</head>
<body>
<div class="canvas">
  <p class="spec-note">4oz stand-up pouch (specifications required)</p>

  <svg class="dieline" width="920" height="1200" viewBox="0 0 920 1200" aria-hidden="true">
    <rect class="pouch-face" x="78" y="62" width="760" height="1040" fill="var(--pouch-yellow)"/>
    <ellipse class="backdrop-swirl" cx="460" cy="640" rx="300" ry="420" fill="var(--deep-yellow)" opacity="0.55"/>
    <ellipse cx="460" cy="640" rx="340" ry="450" fill="none" stroke="var(--cream)" stroke-width="6" opacity="0.35"/>

    <rect x="78" y="62" width="760" height="1040" fill="none" stroke="var(--dieline)" stroke-width="1.2"/>
    <g stroke="var(--dieline)" stroke-width="1" stroke-dasharray="6 5" fill="none">
      <line x1="108" y1="62" x2="108" y2="1102"/>
      <line x1="808" y1="62" x2="808" y2="1102"/>
      <line x1="78" y1="163" x2="838" y2="163"/>
      <line x1="78" y1="213" x2="838" y2="213"/>
      <line x1="78" y1="883" x2="108" y2="883"/>
      <line x1="808" y1="883" x2="838" y2="883"/>
      <path d="M108 883 Q458 1180 808 883"/>
    </g>

    <g class="tear-notches" fill="#ffffff">
      <polygon points="86,189 100,181 100,197"/><polygon points="111,189 125,181 125,197"/>
      <polygon points="136,189 150,181 150,197"/><polygon points="161,189 175,181 175,197"/>
      <polygon points="186,189 200,181 200,197"/><polygon points="211,189 225,181 225,197"/>
      <polygon points="236,189 250,181 250,197"/><polygon points="261,189 275,181 275,197"/>
      <polygon points="286,189 300,181 300,197"/><polygon points="311,189 325,181 325,197"/>
      <polygon points="336,189 350,181 350,197"/><polygon points="361,189 375,181 375,197"/>
      <polygon points="386,189 400,181 400,197"/><polygon points="411,189 425,181 425,197"/>
      <polygon points="436,189 450,181 450,197"/><polygon points="461,189 475,181 475,197"/>
      <polygon points="486,189 500,181 500,197"/><polygon points="511,189 525,181 525,197"/>
      <polygon points="536,189 550,181 550,197"/><polygon points="561,189 575,181 575,197"/>
      <polygon points="586,189 600,181 600,197"/><polygon points="611,189 625,181 625,197"/>
      <polygon points="636,189 650,181 650,197"/><polygon points="661,189 675,181 675,197"/>
      <polygon points="686,189 700,181 700,197"/><polygon points="711,189 725,181 725,197"/>
      <polygon points="736,189 750,181 750,197"/><polygon points="761,189 775,181 775,197"/>
      <polygon points="780,189 796,178 838,178 838,204 796,204"/>
    </g>

    <defs>
      <path id="tagline-arc-top" d="M258 950 Q390 1030 522 975"/>
      <path id="tagline-arc-bottom" d="M312 1010 Q420 1050 535 1002"/>
    </defs>
    <text class="tagline" font-family="'PT Sans', sans-serif" font-size="22" fill="var(--navy)">
      <textPath href="#tagline-arc-top">The perfect mixture between</textPath>
    </text>
    <text class="tagline-strong" font-family="'PT Sans', sans-serif" font-weight="700" font-size="30" fill="var(--navy)">
      <textPath href="#tagline-arc-bottom">sweet and spicy.</textPath>
    </text>
  </svg>

  <div class="brand-name">Torvel</div>
  <div class="product-title">Ginger</div>
  <div class="product-subtitle">Chewy Candy</div>
  <div class="candy-photo" role="img" aria-label="Photograph of sugar-coated candied ginger slices in a pile"></div>
</div>
</body>
</html>
```